Simple elegant business card

General card for a fin and television director.
Just want name, email, phone and address.

Target Market(s)

Prospective employers

Industry/Entity Type

Business

Requirements
Must have
• As above
Nice to have
• Logo but not necessary.
Should not have
• Not too colourful or funky.
• Simplicity and elegance the way to go.

```html
<!DOCTYPE html>
<html lang="en">
<head>
<meta charset="utf-8">
<title>Nora Hale – Business Card</title>
<link rel="stylesheet" href="https://fonts.googleapis.com/css2?family=Source+Sans+3:wght@400&display=swap">
<style>
  :root {
    --backdrop: #e6e7e8;
    --card-glow: #d663a8;
    --card-mid: #c9559f;
    --card-edge: #b84699;
    --ink: #f2c6e3;
    --ink-outline: #4a0f42;
    --card-shadow: rgba(40, 40, 40, 0.55);
  }
  html, body {
    margin: 0;
    padding: 0;
    width: 1200px;
    height: 1000px;
    overflow: hidden;
    background: var(--backdrop);
  }
  .canvas {
    position: relative;
    width: 1200px;
    height: 1000px;
  }
  .card {
    position: absolute;
    left: 197px;
    top: 268px;
    width: 806px;
    height: 465px;
    background: radial-gradient(ellipse 620px 520px at 505px 350px,
      var(--card-glow) 0%, var(--card-mid) 55%, var(--card-edge) 100%);
    box-shadow: 4px 4px 6px var(--card-shadow);
    font-family: "Source Sans 3", "Myriad Pro", sans-serif;
  }
  .contact-line {
    position: absolute;
    margin: 0;
    font-size: 25px;
    line-height: 30px;
    letter-spacing: -0.2px;
    color: var(--ink);
    text-shadow:
      0 0 1px var(--ink-outline),
      0 0 1px var(--ink-outline),
      0 0 2px var(--ink-outline),
      0 1px 3px rgba(74, 15, 66, 0.7);
    white-space: nowrap;
  }
  .contact-address {
    top: 354px;
    left: 50%;
    transform: translateX(-50%);
    font-size: 20px;
  }
  .contact-name,
  .contact-email,
  .contact-phone { top: 396px; }
  .contact-name { left: 45px; }
  .contact-email { left: 390px; transform: translateX(-50%); }
  .contact-phone { right: 46px; }
</style>
</head>
<body>
  <main class="canvas">
    <section class="card" aria-label="Business card">
      <p class="contact-line contact-address">1420 Sunset Avenue, Los Angeles, CA 90026</p>
      <p class="contact-line contact-name">Nora Hale</p>
      <p class="contact-line contact-email">norahale@mail.com</p>
      <p class="contact-line contact-phone">+1 310 555 0142</p>
    </section>
  </main>
</body>
</html>
```